Breezeway Comfort business cards design

Need a business card design for a Heating and Air Conditioning business. I need these items included.
Business name: Breezeway Comfort
Owner: Marcus Tollefsen
License # 2874590
Phone number # 555-382-4071
Email: breezewaycomfortair@mailvista.example
Sales
Service
Installation
Maintenance

Heating and Air Conditioning

Requirements
Must have
• Company name , license number , phone number , email

```html
<!DOCTYPE html>
<html lang="en">
<head>
<meta charset="utf-8">
<title>Breezeway Comfort – Business Cards</title>
<link rel="stylesheet" href="https://fonts.googleapis.com/css2?family=Montserrat:wght@400;500;700&display=swap">
<style>
  :root {
    --bg: #2b2b2b;
    --card-white: #f1f1f1;
    --brand-blue: #1f3fa6;
    --brand-blue-deep: #13308f;
    --brand-blue-light: #3d63c4;
    --brand-orange: #f0702a;
    --ink: #222222;
    --white: #ffffff;
  }
  * { box-sizing: border-box; margin: 0; padding: 0; }
  html, body {
    width: 1200px; height: 880px; overflow: hidden;
    background: var(--bg);
    font-family: "Montserrat", sans-serif;
  }
  .stage {
    width: 1200px; height: 880px;
    display: flex; align-items: center; justify-content: center; gap: 80px;
  }
  .card {
    width: 340px; height: 560px;
    border-radius: 22px;
    position: relative;
    display: flex; flex-direction: column; align-items: center;
    text-align: center;
    box-shadow: 0 18px 40px rgba(0,0,0,.45);
  }
  /* Front */
  .card--front { background: var(--card-white); padding: 64px 30px 48px; }
  .brand-dot {
    width: 26px; height: 26px; border-radius: 50%;
    background: var(--brand-orange);
    margin-top: 120px; margin-bottom: 18px;
  }
  .brand-name {
    font-weight: 700; font-size: 30px; line-height: 1.1;
    color: var(--brand-blue); letter-spacing: .5px;
  }
  .card--back .brand-name { color: var(--white); }
  .brand-sub {
    font-weight: 500; font-size: 15px; letter-spacing: 4px;
    text-transform: uppercase; color: var(--brand-orange); margin-top: 8px;
  }
  .card--back .brand-sub { color: var(--white); }
  .license { font-size: 13px; color: var(--brand-blue); margin-top: 8px; }
  .owner-name {
    font-weight: 700; font-size: 19px; color: var(--brand-blue);
    text-transform: uppercase; margin-top: 24px;
  }
  .owner-role { font-size: 13px; color: var(--brand-blue-light); margin-top: 2px; }
  .contact { margin-top: 32px; display: flex; flex-direction: column; align-items: center; gap: 6px; }
  .contact-icon { width: 12px; height: 12px; fill: var(--brand-blue); }
  .contact-text { font-size: 13px; color: var(--ink); }
  .contact-text--email { font-size: 11.5px; }
  /* Back */
  .card--back {
    background: radial-gradient(circle at 78% 12%, var(--brand-blue-light) 0%, var(--brand-blue) 45%, var(--brand-blue-deep) 100%);
    justify-content: center; padding: 40px 26px;
  }
  .card--back .brand-dot { margin-top: 0; }
  .services {
    position: absolute; bottom: 42px; left: 0; right: 0;
    color: var(--white); font-size: 13px; letter-spacing: 2px; line-height: 1.6;
  }
</style>
</head>
<body>
<main class="stage">
  <section class="card card--front">
    <div class="brand-dot"></div>
    <h1 class="brand-name">Breezeway Comfort</h1>
    <p class="brand-sub">Heating &amp; Air</p>
    <p class="license">License # 2874590</p>
    <h2 class="owner-name">Marcus Tollefsen</h2>
    <p class="owner-role">Owner</p>
    <div class="contact">
      <svg class="contact-icon" viewBox="0 0 24 24"><path d="M6.6 10.8a15 15 0 0 0 6.6 6.6l2.2-2.2c.3-.3.7-.4 1-.2 1.1.4 2.3.6 3.6.6.6 0 1 .4 1 1V20c0 .6-.4 1-1 1A17 17 0 0 1 3 4c0-.6.4-1 1-1h3.5c.6 0 1 .4 1 1 0 1.3.2 2.5.6 3.6.1.3 0 .7-.2 1z"/></svg>
      <p class="contact-text">555-382-4071</p>
      <svg class="contact-icon" viewBox="0 0 24 24"><path d="M2 5h20v14H2zm2 2v.5l8 5 8-5V7zm0 2.8V17h16V9.8l-8 5z"/></svg>
      <p class="contact-text contact-text--email">breezewaycomfortair@mailvista.example</p>
    </div>
  </section>
  <section class="card card--back">
    <div class="brand-dot"></div>
    <h1 class="brand-name">Breezeway Comfort</h1>
    <p class="brand-sub">Heating &amp; Air</p>
    <p class="services">Sales | Service |<br>Installation | Maintenance</p>
  </section>
</main>
</body>
</html>
```